BOLD & MINIMALIST DESIGN NEEDED

We want a very bold but minimalistic business card design that is impactful and utilizes both sides of the business card. Our current logo is included for your use.

We want bold fonts and good use of negative space. We don't want the logo to overpower the design.

Target Market(s)

Professionals who are building new commercial buildings.

Industry/Entity Type

Construction

Contact Information for Business Card

Name, Title, email, office phone, cell phone, website

Font styles to use
Serif
Sans Serif

Requirements
Must have
• Bold design!

```html
<!DOCTYPE html>
<html lang="en">
<head>
<meta charset="utf-8">
<title>Crestline Business Card</title>
<link href="https://fonts.googleapis.com/css2?family=Arimo:wght@400;700&display=swap" rel="stylesheet">
<style>
  :root {
    --stage: #1d1d1d;
    --paper: #f4f4f4;
    --green: #7dbd3c;
    --ink: #2a2a2a;
    --white: #ffffff;
  }
  * { margin: 0; padding: 0; box-sizing: border-box; }
  html, body {
    width: 1200px; height: 1059px; overflow: hidden;
    background: var(--stage);
    font-family: "Arimo", Arial, sans-serif;
  }
  .canvas { position: relative; width: 1200px; height: 1059px; }
  .card {
    position: absolute; left: 256px; width: 690px; height: 391px;
    border-radius: 18px; overflow: hidden;
  }
  .card--front { top: 89px; background: var(--paper); }
  .card--back { top: 547px; background: var(--green); }

  .brand {
    position: absolute; display: flex; align-items: center; gap: 10px;
    font-weight: 700; letter-spacing: 0.5px; white-space: nowrap;
  }
  .brand__square { display: block; flex: none; }
  .card--front .brand {
    left: 0; width: 352px; top: 174px; justify-content: center;
    font-size: 38px; color: var(--ink);
  }
  .card--front .brand__square { width: 22px; height: 22px; background: var(--green); }
  .card--back .brand {
    left: 0; right: 0; top: 160px; justify-content: center;
    font-size: 64px; color: var(--white);
  }
  .card--back .brand__square { width: 36px; height: 36px; background: var(--white); }

  .divider {
    position: absolute; left: 352px; top: 109px; width: 1px; height: 176px;
    background: var(--green); opacity: 0.7;
  }
  .person { position: absolute; left: 378px; top: 108px; }
  .person__name { font-size: 27px; font-weight: 700; color: var(--green); line-height: 1; letter-spacing: 0.3px; }
  .person__title { font-size: 18px; color: var(--ink); margin-top: 3px; }

  .contacts { position: absolute; left: 378px; top: 184px; list-style: none; }
  .contacts li {
    display: flex; align-items: center; gap: 6px; height: 26.5px;
    font-size: 18px; color: var(--ink);
  }
  .contacts svg { width: 12px; height: 12px; fill: var(--green); flex: none; }
</style>
</head>
<body>
<main class="canvas">
  <section class="card card--front" aria-label="Card front">
    <div class="brand"><span class="brand__square"></span>CRESTLINE</div>
    <div class="divider"></div>
    <div class="person">
      <p class="person__name">DORIAN VALE</p>
      <p class="person__title">Owner/CEO</p>
    </div>
    <ul class="contacts">
      <li><svg viewBox="0 0 12 12"><path d="M2.5 1l2 2.2-1 1.3c.8 1.6 2 2.8 3.6 3.6l1.3-1 2.2 2-1.2 1.9C5.6 10.8 1.2 6.4.9 2.2z"/></svg>07 5550 1234</li>
      <li><svg viewBox="0 0 12 12"><path d="M3.5 0h5a1 1 0 0 1 1 1v10a1 1 0 0 1-1 1h-5a1 1 0 0 1-1-1V1a1 1 0 0 1 1-1zm.3 1.3v8h4.4v-8zM6 9.9a.6.6 0 1 0 0 1.2.6.6 0 0 0 0-1.2z"/></svg>0400 555 762</li>
      <li><svg viewBox="0 0 12 12"><path d="M0 2.5h12v7H0zm1 1L6 7l5-3.5v-.2H1z"/></svg>hello@crestlinebuild.com</li>
      <li><svg viewBox="0 0 12 12"><circle cx="6" cy="6" r="5.5"/><path d="M3 3.5l2 .5 1 2-1.5 1 .5 2.5" stroke="#f4f4f4" stroke-width="1" fill="none"/></svg>www.crestlinebuild.com</li>
    </ul>
  </section>

  <section class="card card--back" aria-label="Card back">
    <div class="brand"><span class="brand__square"></span>CRESTLINE</div>
  </section>
</main>
</body>
</html>
```